Cedar Ridge Strong Partners and Households Initiative-Teen

We need a flyer that invites high school students to our program. The students go through healthy relationship education, financial stability and workforce readiness.

We are in five locations, so we need a flyer that we can edit the text to update addresses, dates and any additional information based on our needs.

Attached are the two logo's we would like to use. I have also attached a previous flyer that we created to give you an idea of the text that is included.

In the past we have only promoted the healthy relationship component, but if you are able to incorporate finances (money) and job development (jobs), that would be great.

Industry/Entity Type

School

Requirements
Must have
• Targets high school students
• Make the text available for us to edit
• Our topics is healthy relationship, money and jobs

```html
<!DOCTYPE html>
<html lang="en">
<head>
<meta charset="utf-8">
<title>Healthy Relationship, Money and Jobs – Teen Workshop Flyer</title>
<link rel="stylesheet" href="https://fonts.googleapis.com/css2?family=Lilita+One&family=Roboto:wght@400;500;700;900&display=swap">
<style>
  :root {
    --orange: #f7941d;
    --orange-light: #fbb040;
    --navy: #0d4a70;
    --navy-dark: #0a3a5a;
    --crimson: #c8124f;
    --accent-red: #9e1b32;
    --white: #ffffff;
    --backdrop: #6b6b6b;
    --display: "Lilita One", "Arial Black", sans-serif;
    --body: "Roboto", Arial, sans-serif;
  }
  html, body {
    margin: 0;
    width: 1200px;
    height: 1200px;
    overflow: hidden;
    background: var(--backdrop);
  }
  .flyer {
    position: absolute;
    left: 167px;
    top: 37px;
    width: 866px;
    height: 1126px;
    box-shadow: 0 4px 16px rgba(0,0,0,.35);
  }
  .flyer svg { display: block; width: 100%; height: 100%; }
  .display { font-family: var(--display); }
  .body { font-family: var(--body); }
</style>
</head>
<body>
<main class="flyer">
  <svg viewBox="0 0 460 598" xmlns="http://www.w3.org/2000/svg" aria-label="Workshop flyer">
    <defs>
      <linearGradient id="location-rule" x1="0" x2="1">
        <stop offset="0" stop-color="var(--orange-light)"/>
        <stop offset="1" stop-color="var(--orange)" stop-opacity="0"/>
      </linearGradient>
    </defs>

    <rect class="page" width="460" height="598" fill="var(--white)"/>
    <polygon class="navy-field" points="0,140 460,598 0,598" fill="var(--navy)"/>

    <rect class="header-band" width="460" height="88" fill="var(--orange)"/>
    <text class="display" x="29" y="41" font-size="28" fill="var(--white)">Healthy Relationship,</text>
    <text class="display" x="29" y="70" font-size="28" fill="var(--white)">Money and Jobs</text>

    <text class="body" x="230" y="108" font-size="12.5" fill="var(--navy)" text-anchor="middle">Workshops for High School students on</text>
    <text class="body" x="230" y="126" font-size="12.5" font-weight="700" letter-spacing=".6" fill="var(--navy)" text-anchor="middle">HEALTHY EMOTIONS &amp; ATTITUDES in RELATIONSHIPS</text>

    <g class="partner-program">
      <circle cx="190" cy="163" r="9" fill="var(--orange)"/>
      <text class="body" x="190" y="194" font-size="11" font-weight="500" fill="var(--orange)" text-anchor="middle">CEDAR RIDGE STRONG PARTNERS</text>
    </g>
    <g class="partner-agency">
      <circle cx="340" cy="174" r="8" fill="var(--crimson)"/>
      <text class="body" x="354" y="172" font-size="10" font-weight="700" fill="var(--navy)">Harbor Valley</text>
      <text class="body" x="354" y="184" font-size="10" font-weight="700" fill="var(--navy)">Community Partners</text>
    </g>

    <text class="body" x="301" y="248" font-size="11" font-weight="700" fill="var(--navy)" text-anchor="middle" letter-spacing=".3">TOPICS INCLUDE:</text>

    <polygon class="schedule-band" points="0,283 170,283 228,340 0,340" fill="var(--orange)"/>
    <polygon class="schedule-accent" points="214,340 228,340 228,356" fill="var(--accent-red)"/>
    <text class="display" x="93" y="305" font-size="16" fill="var(--white)" text-anchor="middle">Workshops will</text>
    <text class="display" x="93" y="323" font-size="16" fill="var(--white)" text-anchor="middle">be held every</text>

    <text class="body" x="112" y="356" font-size="10" fill="var(--white)" text-anchor="middle">Wednesday for 10 weeks starting</text>
    <text class="display" x="112" y="374" font-size="15" fill="var(--white)" text-anchor="middle">January 10th.</text>
    <text class="body" x="112" y="393" font-size="10" fill="var(--white)" text-anchor="middle">From 5:30pm—7:30pm</text>

    <rect class="location-rule" x="0" y="406" width="250" height="7" fill="url(#location-rule)"/>
    <text class="body" x="26" y="412" font-size="4.5" font-weight="700" fill="var(--navy-dark)">LOCATION:</text>
    <polygon class="location-band" points="0,418 296,418 362,484 0,484" fill="var(--orange)"/>
    <polygon class="location-accent" points="348,484 362,484 362,499" fill="var(--accent-red)"/>
    <text class="display" x="162" y="436" font-size="14" fill="var(--white)" text-anchor="middle">Maple Commons Family Center</text>
    <text class="body" x="162" y="451" font-size="9.5" fill="var(--white)" text-anchor="middle">1480 Linden Grove Way</text>
    <text class="body" x="162" y="464" font-size="9.5" fill="var(--white)" text-anchor="middle">Cedar Ridge, CA 90210</text>

    <text class="body" x="175" y="497" font-size="10" font-weight="700" fill="var(--white)" text-anchor="middle" letter-spacing=".3">CALL TO RESERVE A SEAT</text>

    <g class="contact mail">
      <circle cx="77" cy="518" r="8" fill="var(--crimson)"/>
      <path d="M77,513.5 a3,3 0 0 1 3,3 c0,2.3 -3,5.5 -3,5.5 s-3,-3.2 -3,-5.5 a3,3 0 0 1 3,-3z" fill="var(--white)"/>
      <circle cx="77" cy="516.6" r="1.1" fill="var(--crimson)"/>
      <text class="body" x="77" y="536" font-size="4" font-weight="700" fill="var(--white)" text-anchor="middle">MAIL US</text>
      <text class="body" x="77" y="542" font-size="3.6" fill="var(--white)" text-anchor="middle">Dana Whitlow, Program</text>
      <text class="body" x="77" y="547" font-size="3.6" fill="var(--white)" text-anchor="middle">Coordinator</text>
    </g>
    <g class="contact phone">
      <circle cx="188" cy="518" r="8" fill="var(--crimson)"/>
      <path d="M184.5,514 l1.8,-0.6 l1.2,2.4 l-1.1,0.9 a6,6 0 0 0 2.9,2.9 l0.9,-1.1 l2.4,1.2 l-0.6,1.8 a7,7 0 0 1 -7.5,-7.5z" fill="var(--white)"/>
      <text class="body" x="188" y="536" font-size="4" font-weight="700" fill="var(--white)" text-anchor="middle">CALL US</text>
      <text class="body" x="188" y="542" font-size="3.6" fill="var(--white)" text-anchor="middle">General Information</text>
      <text class="body" x="188" y="547" font-size="3.6" fill="var(--white)" text-anchor="middle">(555) 014-2286</text>
    </g>
    <g class="contact email">
      <circle cx="298" cy="518" r="8" fill="var(--crimson)"/>
      <rect x="293.5" y="515" width="9" height="6" rx=".6" fill="var(--white)"/>
      <path d="M293.8,515.4 l4.2,3.2 l4.2,-3.2" fill="none" stroke="var(--crimson)" stroke-width=".7"/>
      <text class="body" x="298" y="536" font-size="4" font-weight="700" fill="var(--white)" text-anchor="middle">E-MAIL US</text>
      <text class="body" x="298" y="542" font-size="3.6" fill="var(--white)" text-anchor="middle">dwhitlow@cedarridge-ci.org</text>
    </g>

    <text class="body funding-note" x="310" y="566" font-size="3.6" fill="var(--white)" text-anchor="middle">Funding for this project was provided by the Cedar Ridge</text>
    <text class="body funding-note" x="208" y="573" font-size="3.6" fill="var(--white)" text-anchor="middle">Youth Futures Fund, Community Grants Program, Grant #00XX0000. These services are available to all eligible students and families.</text>

    <g class="topic recognizing">
      <circle cx="277" cy="305" r="49" fill="var(--white)" stroke="var(--orange)" stroke-width="1.6"/>
      <text class="body" x="277" y="296" font-size="9.5" font-weight="500" fill="var(--navy)" text-anchor="middle">Recognizing</text>
      <text class="body" x="277" y="309" font-size="9" font-weight="500" fill="var(--navy)" text-anchor="middle">signs and types</text>
      <text class="body" x="277" y="322" font-size="9" font-weight="500" fill="var(--navy)" text-anchor="middle">of abuse</text>
    </g>
    <g class="topic building">
      <circle cx="381" cy="297" r="49" fill="var(--white)" stroke="var(--navy)" stroke-width="1" stroke-dasharray="2.5 2"/>
      <text class="body" x="381" y="288" font-size="9.5" font-weight="500" fill="var(--navy)" text-anchor="middle">Building</text>
      <text class="body" x="381" y="302" font-size="9.5" font-weight="500" fill="var(--navy)" text-anchor="middle">Healthy</text>
      <text class="body" x="381" y="316" font-size="9.5" font-weight="500" fill="var(--navy)" text-anchor="middle">relationships</text>
    </g>
    <g class="topic self-esteem">
      <circle cx="286" cy="370" r="31" fill="var(--white)" stroke="var(--crimson)" stroke-width="1" stroke-dasharray="2.5 2"/>
    </g>
    <g class="topic safety">
      <circle cx="348" cy="380" r="45" fill="var(--crimson)"/>
      <text class="body" x="348" y="377" font-size="10" font-weight="700" fill="var(--orange-light)" text-anchor="middle">Safety</text>
      <text class="body" x="348" y="391" font-size="10" font-weight="700" fill="var(--orange-light)" text-anchor="middle">Planning</text>
    </g>
    <text class="body self-esteem-label" x="278" y="373" font-size="6.8" font-weight="500" fill="var(--navy)" text-anchor="middle">Self-esteem</text>
    <g class="topic get-help">
      <circle cx="389" cy="441" r="42" fill="var(--white)" stroke="var(--navy)" stroke-width="1.4"/>
      <text class="body" x="389" y="431" font-size="9.5" font-weight="500" fill="var(--navy)" text-anchor="middle">How to get</text>
      <text class="body" x="389" y="444" font-size="9.5" font-weight="500" fill="var(--navy)" text-anchor="middle">help and</text>
      <text class="body" x="389" y="457" font-size="9.5" font-weight="500" fill="var(--navy)" text-anchor="middle">where</text>
    </g>
  </svg>
</main>
</body>
</html>
```